HARBORLINE AUTO GLASS

Mobile Glass Shop:

1) Windshield REPAIR 2)Windshield replacment 3) Rear Windshield Replacment 4) Side Window Replacment 5) car window replacment 6) Power Window Repair.

Schedual a service within 24 hour with one of our certified technicians.

See "brightvane auto repair" web site for referance on the nature of our buisness and service. www.brightvane-example.com

```html
<!DOCTYPE html>
<html lang="en">
<head>
<meta charset="utf-8">
<title>Harborline Auto Glass</title>
<link href="https://fonts.googleapis.com/css2?family=Roboto:wght@400;500;700&display=swap" rel="stylesheet">
<style>
:root{
  --blue:#1a9ad6;
  --navy:#1d3d66;
  --navy-deep:#19355a;
  --ink:#1b1b1b;
  --muted:#6f6f6f;
  --soft:#f5f5f6;
  --white:#ffffff;
  --line:#e6e6e6;
}
*{box-sizing:border-box;margin:0;padding:0}
html,body{width:1200px;height:3272px;overflow:hidden}
body{font-family:'Roboto',sans-serif;color:var(--ink);background:var(--white);position:relative}
.abs{position:absolute}
.center-x{left:0;width:1200px;text-align:center}

/* top bar */
.topbar{top:0;left:0;width:1200px;height:34px;background:var(--blue);color:var(--white);font-size:11px}
.topbar span{position:absolute;top:11px;display:flex;align-items:center;gap:6px}
/* nav */
.nav{top:34px;left:0;width:1200px;height:73px;background:var(--white)}
.brand{position:absolute;left:108px;top:22px;display:flex;align-items:center;gap:8px;font-weight:700;font-size:15px;color:var(--blue)}
.brand i{display:block;width:26px;height:30px;background:var(--blue)}
.menu{position:absolute;top:30px;left:536px;display:flex;gap:28px;font-size:12px;color:var(--ink)}
.btn{display:flex;align-items:center;justify-content:center;border-radius:20px;font-size:11px;font-weight:500;color:var(--white);background:var(--blue);text-transform:uppercase}
.nav .btn{position:absolute;left:955px;top:21px;width:140px;height:34px}

/* hero */
.hero{top:107px;left:0;width:1200px;height:483px;background:linear-gradient(120deg,#3c4a58 0%,#6b7884 40%,#8a8f8c 65%,#4d5660 100%)}
.hero-kicker{top:257px;font-size:12px;color:#3aaee6}
.hero-title{top:296px;font-size:33px;font-weight:400;color:var(--white)}
.hero-text{top:351px;font-size:11px;line-height:14px;color:var(--white)}
.hero .btn{position:absolute}
.dots span{position:absolute;height:2px;width:28px;background:var(--white)}

/* sections */
.kicker{font-size:11px;color:var(--blue);text-transform:uppercase}
.heading{font-size:33px;font-weight:500;color:var(--ink)}
.services{top:590px;left:0;width:1200px;height:747px;background:var(--soft)}
.intro{font-size:11px;line-height:18px;color:var(--muted)}
.intro b{color:#444;font-weight:500}
.card{position:absolute;width:225px;height:217px;background:var(--white);text-align:center;box-shadow:0 1px 3px rgba(0,0,0,.05)}
.card svg{position:absolute;left:88px;top:40px}
.card h3{position:absolute;left:0;top:98px;width:225px;font-size:15px;font-weight:500;color:var(--ink)}
.card p{position:absolute;left:20px;top:134px;width:185px;font-size:11px;line-height:18px;color:var(--muted)}
.card.active{background:var(--blue)}
.card.active h3,.card.active p{color:var(--white)}

.photo{position:absolute;top:1521px;height:206px}

/* quote */
.quote{top:1855px;left:0;width:1193px;height:478px;background:var(--navy)}
.field{position:absolute;border:1px solid rgba(255,255,255,.35);color:rgba(255,255,255,.7);font-size:11px;padding:0 15px;display:flex;align-items:center}
.outline{border:1px solid rgba(255,255,255,.6);background:transparent}

/* testimonials */
.tcard{position:absolute;top:2480px;width:372px;height:196px;background:var(--white);box-shadow:0 2px 10px rgba(0,0,0,.08)}
.avatar{position:absolute;top:-12px;left:54px;width:56px;height:56px;border-radius:50%;background:radial-gradient(circle at 50% 40%,#e6c8a8,#b08e72);border:3px solid var(--white);box-shadow:0 1px 4px rgba(0,0,0,.15)}
.tcard p{position:absolute;left:58px;top:68px;width:290px;font-size:11px;line-height:18px;color:var(--muted)}
.tname{position:absolute;left:248px;top:150px;font-size:13px;font-weight:500;width:80px;text-align:center}
.stars{position:absolute;left:252px;top:167px;font-size:8px;color:#f0a500;letter-spacing:1px}
.qbadge{position:absolute;left:50px;top:150px;width:36px;height:46px;background:var(--blue);border-radius:18px 18px 0 0}
.arrow-sq{position:absolute;top:2722px;width:26px;height:24px;background:var(--ink);color:var(--white);font-size:11px;display:flex;align-items:center;justify-content:center}

/* footer */
.footer{top:2866px;left:0;width:1200px;height:406px;background:var(--navy-deep)}
.partners{top:2800px;left:105px;width:990px;height:139px;background:var(--blue)}
.plogo{position:absolute;top:56px;height:26px;width:84px;border-radius:4px;background:rgba(255,255,255,.35)}
.fhead{position:absolute;top:2996px;font-size:12px;font-weight:500;color:var(--white)}
.flinks{position:absolute;top:3033px;font-size:9.5px;line-height:21px;color:var(--white)}
.ftext{font-size:9.5px;line-height:13.5px;color:var(--white)}
.sub{position:absolute;left:885px;width:182px;height:30px;background:var(--white);font-size:9.5px;padding-left:18px;display:flex;align-items:center;color:#333}
.social{position:absolute;top:3227px;width:18px;height:18px;border-radius:50%;background:var(--blue)}
</style>
</head>
<body>

<div class="abs topbar">
  <span style="left:120px">Welcome to Harborline Auto Glass Any Help Contact Us</span>
  <span style="left:434px">
    <svg width="16" height="16" viewBox="0 0 16 16"><circle cx="8" cy="8" r="8" fill="#fff"/><path d="M5 4.5l1.5-.5 1 2-1 .8a5 5 0 0 0 2.7 2.7l.8-1 2 1-.5 1.5c-3.5 0-6.5-3-6.5-6.5z" fill="#1a9ad6"/></svg>
    +012-(345)-55501842</span>
  <span style="left:778px">
    <svg width="10" height="12" viewBox="0 0 10 12"><path d="M5 11S1 7 1 4.5a4 4 0 0 1 8 0C9 7 5 11 5 11z" fill="none" stroke="#fff"/><circle cx="5" cy="4.5" r="1.3" fill="none" stroke="#fff"/></svg>
    48 Pier Lane, Harbor City</span>
  <span style="left:957px">
    <svg width="12" height="10" viewBox="0 0 12 10"><rect x=".5" y=".5" width="11" height="9" fill="none" stroke="#fff"/><path d="M.5 .5L6 5l5.5-4.5" fill="none" stroke="#fff"/></svg>
    support@harborline-example.com</span>
</div>

<header class="abs nav">
  <div class="brand"><i></i>HARBORLINE</div>
  <nav class="menu">
    <span>Services &#8964;</span><span>Locations</span><span>We’re hiring</span><span>My appointment</span>
  </nav>
  <div class="btn">Get Quote</div>
</header>

<section class="abs hero" role="img" aria-label="Smiling man reclining on the hood of a silver car by a rocky shore"></section>
<div class="abs center-x hero-kicker">WELCOME TO THE HARBORLINE AUTO GLASS</div>
<h1 class="abs center-x hero-title">WE PROVIDE 24/7 MOBILE SERVICE</h1>
<p class="abs center-x hero-text">We Offer FREE mobile repair service, for all customers<br>within a 25 mile range of our location.</p>
<div class="abs btn" style="left:530px;top:408px;width:138px;height:33px">Get Quote</div>
<div class="dots">
  <span style="left:555px;top:554px"></span>
  <span style="left:587px;top:554px;background:var(--blue)"></span>
  <span style="left:619px;top:554px"></span>
</div>

<section class="abs services">
  <div class="abs center-x kicker" style="top:72px">Our Services</div>
  <h2 class="abs center-x heading" style="top:100px">What We Offer For You</h2>
  <p class="abs center-x intro" style="top:150px"><b>HARBORLINE AUTO GLASS</b> is incredibly flexible, friendly and easy to work with. Our list<br>of services are widely acknowledged to assure you get the best quality service;</p>

  <div class="card active" style="left:244px;top:223px">
    <svg width="50" height="34" viewBox="0 0 50 34"><path d="M4 6q21-6 42 0l-3 22q-18-4-36 0z" fill="none" stroke="#fff" stroke-width="1.6"/><path d="M25 9l2 5 5-2-3 5 5 2-6 1 1 5-4-4-4 4 1-5-6-1 5-2-3-5 5 2z" fill="none" stroke="#fff" stroke-width="1.2"/></svg>
    <h3>Windshield REPAIR</h3>
    <p>An important thing to know about car maintenance reminder systems, especially those</p>
  </div>
  <div class="card" style="left:489px;top:223px">
    <svg width="50" height="34" viewBox="0 0 50 34"><path d="M4 6q21-6 42 0l-3 22q-18-4-36 0z" fill="none" stroke="#1a6fb0" stroke-width="1.6"/><path d="M9 10q16-4 32 0l-2 13q-14-3-28 0z" fill="none" stroke="#1a6fb0" stroke-width="1.2"/></svg>
    <h3>Windshield replacment</h3>
    <p>An important thing to know about car maintenance reminder systems, especially those</p>
  </div>
  <div class="card" style="left:734px;top:223px">
    <svg width="50" height="34" viewBox="0 0 50 34"><path d="M4 8q21-5 42 0l-2 18H6z" fill="none" stroke="#1a6fb0" stroke-width="1.6"/><path d="M20 26q5-3 10 0" fill="none" stroke="#1a6fb0" stroke-width="1.2"/></svg>
    <h3>Rear Windshield Replacment</h3>
    <p>An important thing to know about car maintenance reminder systems, especially those</p>
  </div>
  <div class="card" style="left:244px;top:460px">
    <svg width="50" height="34" viewBox="0 0 50 34"><path d="M2 6q23-8 46 0L25 33z" fill="none" stroke="#1a6fb0" stroke-width="1.6"/><path d="M20 12v12M25 10v15M30 12v12M17 16l3-2 3 2M22 14l3-2 3 2M27 16l3-2 3 2" fill="none" stroke="#1a6fb0" stroke-width="1.2"/></svg>
    <h3>Side Window Replacment</h3>
    <p>An important thing to know about car maintenance reminder systems, especially those</p>
  </div>
  <div class="card" style="left:489px;top:460px">
    <svg width="50" height="34" viewBox="0 0 50 34"><path d="M3 30V16l10-12h30v26z" fill="none" stroke="#1a6fb0" stroke-width="1.6"/><path d="M16 8h24v10H9z" fill="none" stroke="#1a6fb0" stroke-width="1.2"/><path d="M3 24h40" stroke="#1a6fb0" stroke-width="1.2"/><path d="M28 10l-3 5M32 10l-3 5" stroke="#1a6fb0"/></svg>
    <h3>Car Window Replacment</h3>
    <p>An important thing to know about car maintenance reminder systems, especially those</p>
  </div>
  <div class="card" style="left:734px;top:460px">
    <svg width="50" height="34" viewBox="0 0 50 34"><rect x="3" y="4" width="18" height="16" fill="none" stroke="#1a6fb0" stroke-width="1.4"/><path d="M14 8h30l4 10v10H10V18z" fill="none" stroke="#1a6fb0" stroke-width="1.6"/><path d="M17 11h24l2 6H15z" fill="none" stroke="#1a6fb0" stroke-width="1.2"/><circle cx="18" cy="29" r="3" fill="none" stroke="#1a6fb0" stroke-width="1.4"/><circle cx="40" cy="29" r="3" fill="none" stroke="#1a6fb0" stroke-width="1.4"/></svg>
    <h3>Power Window Repair</h3>
    <p>An important thing to know about car maintenance reminder systems, especially those</p>
  </div>
</section>

<div class="abs center-x kicker" style="top:1408px">Photo Gallery</div>
<h2 class="abs center-x heading" style="top:1433px">Our Recent Latest Photo Gallery</h2>
<div class="photo" style="left:0;width:295px;background:linear-gradient(135deg,#b6a68c,#8d8a86 55%,#6e6a64)" role="img" aria-label="Technician fitting glass into the door of a silver car"></div>
<div class="photo" style="left:301px;width:295px;background:linear-gradient(160deg,#3f7fb5,#2b5d8e 50%,#23344a)" role="img" aria-label="Businessman in a suit standing by a dark car outside a glass office building"></div>
<div class="photo" style="left:603px;width:295px;background:linear-gradient(135deg,#c9d4c2,#9fae9c 50%,#3a3a3a)" role="img" aria-label="Hooded person breaking into a white car window"></div>
<div class="photo" style="left:904px;width:296px;background:linear-gradient(135deg,#6b6d6a,#8c8b86 50%,#4f524f)" role="img" aria-label="Woman behind a rain-streaked car window"></div>
<svg class="abs" style="left:580px;top:1774px" width="40" height="10" viewBox="0 0 40 10"><circle cx="5" cy="5" r="2.5" fill="#aaa"/><circle cx="13" cy="5" r="2.5" fill="#aaa"/><rect x="19" y="2.5" width="18" height="5" rx="2.5" fill="#1a6fb0"/></svg>

<section class="abs quote" role="group" aria-label="Get quote form on a faint map background">
  <div class="abs" style="left:105px;top:70px;font-size:11px;color:var(--white)">CONTACT US</div>
  <h2 class="abs" style="left:105px;top:98px;font-size:33px;font-weight:500;color:var(--white)">Get Quote Today</h2>
  <div class="field" style="left:105px;top:158px;width:228px;height:43px">Your Full Name</div>
  <div class="field" style="left:358px;top:158px;width:227px;height:43px">Your Phone Number</div>
  <div class="field" style="left:615px;top:158px;width:227px;height:43px">Your Email Address</div>
  <div class="field" style="left:867px;top:158px;width:228px;height:43px;justify-content:space-between">Best time for service
    <svg width="14" height="8" viewBox="0 0 14 8"><path d="M1 1l6 6 6-6" fill="none" stroke="#1a9ad6" stroke-width="1.8"/></svg></div>
  <div class="field" style="left:105px;top:221px;width:990px;height:110px;align-items:flex-start;padding-top:15px">Your question</div>
  <div class="abs btn" style="left:108px;top:378px;width:138px;height:34px">Send Now</div>
  <div class="abs btn outline" style="left:259px;top:378px;width:154px;height:34px">Our Contacts</div>
</section>

<div class="abs kicker" style="left:0;width:1180px;text-align:center;top:2372px">Testimonials</div>
<h2 class="abs heading" style="left:0;width:1180px;text-align:center;top:2397px">What Our Clients Said</h2>

<div class="tcard" style="left:215px">
  <div class="avatar" role="img" aria-label="Portrait of a smiling woman"></div>
  <p>I replace my door glass &amp; windshield, great price and services. Willing to do mobile service.</p>
  <div class="qbadge"></div>
  <div class="tname">Mara Quinlan</div>
  <div class="stars">★★★★☆</div>
</div>
<div class="tcard" style="left:615px">
  <div class="avatar" role="img" aria-label="Portrait of a young man"></div>
  <p>Very friendly, excellent customer service, very professional extremely helpful, is knowledgeable.</p>
  <div class="qbadge"></div>
  <div class="tname">Owen Hadley</div>
  <div class="stars">★★★★★</div>
</div>
<div class="arrow-sq" style="left:571px">&lsaquo;</div>
<div class="arrow-sq" style="left:603px">&rsaquo;</div>

<footer class="abs footer"></footer>
<div class="abs partners">
  <svg class="abs" style="left:41px;top:46px" width="48" height="48" viewBox="0 0 48 48"><circle cx="24" cy="24" r="24" fill="rgba(255,255,255,.3)"/><path d="M34 24H14m7-7l-7 7 7 7" fill="none" stroke="#1a9ad6" stroke-width="2.5"/></svg>
  <div class="plogo" style="left:130px"></div>
  <div class="plogo" style="left:288px"></div>
  <div class="plogo" style="left:440px"></div>
  <div class="plogo" style="left:600px"></div>
  <div class="plogo" style="left:765px"></div>
  <svg class="abs" style="left:901px;top:46px" width="48" height="48" viewBox="0 0 48 48"><circle cx="24" cy="24" r="24" fill="#fff"/><path d="M14 24h20m-7-7l7 7-7 7" fill="none" stroke="#1a9ad6" stroke-width="2.5"/></svg>
</div>

<div class="fhead" style="left:107px;top:2991px">About Harborline</div>
<div class="abs" style="left:110px;top:3032px;display:flex;align-items:center;gap:6px;font-weight:700;font-size:12px;color:var(--blue)"><i style="display:block;width:20px;height:24px;background:var(--blue)"></i>HARBORLINE</div>
<p class="abs ftext" style="left:106px;top:3072px;width:205px">Sed ut perspiciatis unde omnis iste natus error sit volu ptatem accusantium remque laudantiue totam rem aperiam, eaque ipsa quae ab illo inventore veritatis architecto beatae vitae dicta</p>
<div class="abs" style="left:106px;top:3158px;display:flex;align-items:center;gap:6px;font-size:11px;font-weight:500;color:var(--white)">
  <svg width="18" height="14" viewBox="0 0 18 14"><rect x="1" y="1" width="16" height="12" fill="none" stroke="#1a9ad6" stroke-width="1.4"/><path d="M1 1l8 7 8-7" fill="none" stroke="#1a9ad6" stroke-width="1.4"/></svg>
  support@harborline-example.com</div>

<div class="fhead" style="left:385px">Quick Linkst</div>
<div class="flinks" style="left:385px">About Us<br>Locations<br>We’re hiring<br>My appointment<br>Gallery<br>Contact Us</div>

<div class="fhead" style="left:633px">Services</div>
<div class="flinks" style="left:633px">Windshield REPAIR<br>Windshield replacment<br>Rear Windshield Replacment<br>Side Window Replacment<br>car window replacment<br>Power Window Repair</div>

<div class="fhead" style="left:884px">Subscribe Today</div>
<div class="sub" style="top:3028px">Name</div>
<div class="sub" style="top:3066px">Email</div>
<div class="abs btn" style="left:885px;top:3109px;width:88px;height:30px;border-radius:0;text-transform:none;font-size:9.5px">Subscribe</div>

<div class="abs" style="left:105px;top:3205px;width:990px;height:1px;background:rgba(255,255,255,.25)"></div>
<div class="abs" style="left:105px;top:3231px;font-size:10px;color:rgba(255,255,255,.75)">Copyright © 2022 HARBORLINE AUTO GLASS. All Rights Reserved.</div>
<div class="social" style="left:966px"></div>
<div class="social" style="left:1003px"></div>
<div class="social" style="left:1039px"></div>
<div class="social" style="left:1076px"></div>

</body>
</html>
```